M.O.R.K.A.D. Infographic

I need I do need an infographic based on the 6 elements of my curriculum using the imagery of a path with a sunrise at the end.
The attached is a poor rendering with lots of mistakes and missing info but you can use this as a starting point. Here is a description of what I need:
Headline:
Thriving Every Day Beyond Quiet Years: M.O.R.K.A.D.
6 Elements of the M.O.R.K.A.D. curriculum:
Learn to Adapt to Hearing Loss - with the proper use of the right technology and communication strategies
Interact with Purpose – for more fulfilling relationships
Sustain Vitality – with effective habits for mental and physical health
Embrace Growth – to enjoy the benefits of lifelong learning
Nurture Motivation – to continue progressing
Use the following brand colors and fonts:
Hex colors:
#65A4DB Blue
#F1DC75 Yellow
#DB9C65 Sienna
#AAB47A Green
Fonts:
Open Sans font for (headlines)
Lora Google font for (subhead and text)

```html
<!DOCTYPE html>
<html lang="en">
<head>
<meta charset="utf-8">
<title>Thriving Every Day Beyond Quiet Years: M.O.R.K.A.D.</title>
<link rel="stylesheet" href="https://fonts.googleapis.com/css2?family=Fira+Sans:wght@300;400;500;600&display=swap">
<style>
  :root {
    --frame: #000000;
    --cream: #efe6c9;
    --ink: #0e3a48;
    --sky: #a9d3d4;
    --hill: #5f8f4b;
    --valley: #1d5a4f;
    --deep: #063a48;
    --sienna: #c1783b;
    --sun: #f0c14b;
    --leaf: #6b9a4d;
    --lake: #1b779b;
    --white: #ffffff;
    --head: "Fira Sans", sans-serif;
  }
  * { box-sizing: border-box; margin: 0; padding: 0; }
  html, body { width: 839px; height: 1200px; overflow: hidden; background: var(--frame); }
  .poster {
    position: absolute; left: 46px; top: 42px;
    width: 747px; height: 1120px;
    background: var(--cream); overflow: hidden;
    font-family: var(--head);
  }
  .title {
    position: absolute; left: 0; right: 0; top: 40px;
    text-align: center; color: var(--ink);
    font-weight: 600; font-size: 52px; line-height: 61px;
    letter-spacing: -0.5px;
  }
  .subtitle {
    position: absolute; left: 0; right: 0; top: 226px;
    text-align: center; color: var(--ink);
    font-weight: 400; font-size: 27px;
  }
  .landscape {
    position: absolute; left: 0; right: 0; top: 283px; bottom: 0;
    background: linear-gradient(180deg, var(--sky) 0%, var(--cream) 14%, var(--hill) 24%, var(--valley) 48%, var(--deep) 100%);
  }
  .element {
    position: absolute; border-radius: 10px;
    color: var(--white); text-align: center;
    display: flex; flex-direction: column; justify-content: center;
    padding: 8px 10px;
  }
  .element h2 { font-weight: 500; font-size: 28px; line-height: 33px; }
  .element p { font-weight: 300; font-size: 19.5px; line-height: 25px; margin-top: 4px; }
  .interact { left: 42px; top: 461px; width: 190px; height: 152px; background: var(--sienna); }
  .embrace  { left: 514px; top: 517px; width: 191px; height: 156px; background: var(--sun); }
  .sustain  { left: 42px; top: 667px; width: 190px; height: 168px; background: var(--leaf); }
  .learn    { left: 42px; top: 897px; width: 276px; height: 172px; background: var(--lake); }
  .nurture  { left: 512px; top: 883px; width: 192px; height: 147px; background: var(--leaf); }
</style>
</head>
<body>
  <main class="poster">
    <h1 class="title">Thriving Every Day<br>Beyond Quiet Years:<br>M.O.R.K.A.D.</h1>
    <p class="subtitle">6 Elements of the M.O.R.K.A.D. curriculum</p>
    <div class="landscape" role="img" aria-label="Rolling green hills with a winding orange path leading to a rising sun between pale blue clouds"></div>

    <section class="element interact">
      <h2>Interact<br>with Purpose</h2>
      <p>for more fulfilling relationships</p>
    </section>
    <section class="element embrace">
      <h2>Embrace<br>Growth</h2>
      <p>to enjoy the benefits of lifelong learning</p>
    </section>
    <section class="element sustain">
      <h2>Sustain<br>Vitality</h2>
      <p>with effective habits for mental and physical health</p>
    </section>
    <section class="element learn">
      <h2>Learn to Adapt<br>to Hearing Loss</h2>
      <p>with the proper use of the right technology and communication strategies</p>
    </section>
    <section class="element nurture">
      <h2>Nurture<br>Motivation</h2>
      <p>to continue progressing</p>
    </section>
  </main>
</body>
</html>
```